Cube truck ZPL derola 2018 12ft roofing company wraping

ZPL derola 2018 12 ft want something similar to the truck design you did.

needs to display all the same informations

Add alot of black since the cube is white

if possible put pictures of real pretigious houses faded in the background of the design

place a logo on the front of the cube but nothing on the doors or hood

```html
<!DOCTYPE html>
<html lang="fr">
<head>
<meta charset="utf-8">
<title>Les Toitures Velmar – habillage de camion cube</title>
<link rel="stylesheet" href="https://fonts.googleapis.com/css2?family=Oswald:wght@300;500&family=Montserrat:wght@600;700&display=swap">
<style>
  :root {
    --ink: #000000;
    --sky-blue: #1ea8d6;
    --white: #ffffff;
    --backdrop: #e9edf1;
    --slate: #3a4556;
    --cedar: #5a3426;
    --leaf: #6f8a55;
    --siding: #c9ccd0;
  }
  html, body {
    margin: 0;
    width: 1200px;
    height: 846px;
    overflow: hidden;
    background: var(--backdrop);
  }
  .canvas {
    position: relative;
    width: 1200px;
    height: 846px;
  }
  .panel {
    position: absolute;
    top: 213px;
    height: 420px;
    background: var(--ink);
    box-shadow: 0 4px 18px rgba(0,0,0,.18);
  }
  .side-panel { left: 40px; width: 740px; }
  .front-panel { left: 820px; width: 340px; }
  .panel svg { display: block; }

  .headline { font-family: "Oswald", sans-serif; font-weight: 300; fill: var(--sky-blue); }
  .service  { font-family: "Oswald", sans-serif; font-weight: 300; fill: var(--white); font-size: 36px; }
  .bullet   { fill: var(--sky-blue); }
  .offer    { font-family: "Oswald", sans-serif; font-weight: 300; fill: var(--sky-blue); font-size: 25px; }
  .phone    { font-family: "Oswald", sans-serif; font-weight: 500; fill: var(--white); font-size: 32px; }
  .footer-web { font-family: "Oswald", sans-serif; font-weight: 300; fill: var(--sky-blue); font-size: 15px; }
  .footer-rbq { font-family: "Oswald", sans-serif; font-weight: 300; fill: var(--white); font-size: 16px; }

  .brand-small { font-family: "Montserrat", sans-serif; font-weight: 700; fill: var(--white); font-size: 26px; }
  .brand-name  { font-family: "Montserrat", sans-serif; font-weight: 700; fill: var(--white); font-size: 54px; }
  .brand-inc   { font-family: "Montserrat", sans-serif; font-weight: 700; fill: var(--white); font-size: 18px; }
  .brand-info  { font-family: "Montserrat", sans-serif; font-weight: 600; fill: var(--sky-blue); font-size: 14px; }
</style>
</head>
<body>
<main class="canvas">

  <section class="panel side-panel" aria-label="Côté du cube">
    <svg width="740" height="420" viewBox="0 0 740 420">
      <defs>
        <linearGradient id="house-backdrop" x1="0" y1="0" x2="1" y2="1">
          <stop offset="0" stop-color="var(--slate)"/>
          <stop offset="0.55" stop-color="var(--cedar)"/>
          <stop offset="1" stop-color="#2b1a14"/>
        </linearGradient>
        <linearGradient id="photo-tone" x1="0" y1="0" x2="0" y2="1">
          <stop offset="0" stop-color="#b9c9d8"/>
          <stop offset="0.5" stop-color="var(--siding)"/>
          <stop offset="1" stop-color="var(--leaf)"/>
        </linearGradient>
      </defs>

      <polygon class="house-backdrop" role="img" aria-label="Photo estompée d'une maison prestigieuse au toit de bardeaux"
               points="330,0 740,0 740,420 160,420" fill="url(#house-backdrop)" opacity="0.75"/>

      <polygon class="house-photo" role="img" aria-label="Photo d'une grande maison blanche au toit de métal"
               points="12,28 238,10 196,160 12,178" fill="url(#photo-tone)"/>
      <polygon class="house-photo" role="img" aria-label="Photo d'une maison à pignons entourée d'arbres"
               points="12,192 190,180 152,300 12,310" fill="url(#photo-tone)"/>
      <polygon class="house-photo" role="img" aria-label="Photo d'une maison de campagne au toit vert"
               points="12,324 148,316 112,402 12,408" fill="url(#photo-tone)"/>

      <polygon class="accent-band" points="258,0 302,0 78,420 34,420" fill="var(--sky-blue)"/>
      <polygon class="accent-stripe" points="740,165 740,215 612,420 568,420" fill="var(--sky-blue)"/>
      <polygon class="accent-stripe" points="740,300 740,350 700,420 650,420" fill="var(--sky-blue)" opacity="0.9"/>

      <text class="headline" x="470" y="68" font-size="38">Résidentiel &amp;</text>
      <text class="headline" x="460" y="114" font-size="42">Commercial</text>

      <polygon class="bullet" points="442,160 454,171 442,182"/>
      <text class="service" x="460" y="184">Inspéction</text>
      <polygon class="bullet" points="436,215 448,226 436,237"/>
      <text class="service" x="454" y="239">Réparation</text>
      <polygon class="bullet" points="430,270 442,281 430,292"/>
      <text class="service" x="448" y="294">Réfecion</text>

      <text class="offer" x="310" y="342">Estimation gratuite</text>
      <text class="phone" x="316" y="384">(514) 555-0148</text>

      <text class="footer-web" x="220" y="408">www.toituresvelmar.com</text>
      <text class="footer-rbq" x="370" y="408">RBQ:4820-1137-05</text>
    </svg>
  </section>

  <section class="panel front-panel" aria-label="Devant du cube">
    <svg width="340" height="420" viewBox="0 0 340 420">
      <text class="brand-small" x="28" y="62">Les Toitures</text>
      <rect class="brand-mark" x="28" y="88" width="18" height="18" fill="var(--sky-blue)"/>
      <text class="brand-name" x="56" y="128">VELMAR</text>
      <text class="brand-inc" x="272" y="160">Inc.</text>
      <text class="brand-info" x="56" y="156">RBQ:4820-1137-05</text>
      <text class="brand-info" x="56" y="176">www.toituresvelmar.com</text>
    </svg>
  </section>

</main>
</body>
</html>
```